Corporate consulting business needs a business card

I want a professional business card.... surprise me

Updates

Reason: i dont think 2 days is enough

Target Market(s)

Corprorate and Not for Profit firms and organisations

Industry/Entity Type

Consulting

Contact Information for Business Card

Logo
Corporate Consulting Services
Clear Advice, Steady Delivery, Lasting Value
Tovan Presfield
Director
0427 31 94 62 (Larger)
tovan@tp-advisory.com.au
www.tp-advisory.com.au
include little icons beside the contact info:

- Envelope = email
- Phone = phone
- Globe = website

Font styles to use
Serif
Sans Serif

Requirements
Must have
• Professional and clean
Nice to have
• you tell me

```html
<!DOCTYPE html>
<html lang="en">
<head>
<meta charset="UTF-8">
<title>TP Advisory Services — Business Card</title>
<link rel="stylesheet" href="https://fonts.googleapis.com/css2?family=Cinzel:wght@700&family=Open+Sans:wght@400&display=swap">
<style>
  :root {
    --backdrop: #ece7df;
    --card-light: #f1f1f0;
    --card-dark: #23262a;
    --ink: #3d3d3d;
    --ink-soft: #555555;
    --brand-brown: #4a3428;
    --silver: #c9c9c9;
    --silver-dim: #a7a7a7;
  }
  * { margin: 0; padding: 0; box-sizing: border-box; }
  html, body {
    width: 1200px;
    height: 443px;
    overflow: hidden;
    background: var(--backdrop);
  }
  .canvas {
    position: relative;
    width: 1200px;
    height: 443px;
  }
  .card {
    position: absolute;
    top: 90px;
    width: 479px;
    height: 274px;
    border-radius: 16px;
    box-shadow: 0 2px 6px rgba(0,0,0,0.18);
  }
  .card--front { left: 102px; background: var(--card-light); }
  .card--back  { left: 624px; background: var(--card-dark); }

  .contact__name {
    position: absolute;
    left: 15px; top: 20px;
    font: 400 18px/1 "Open Sans", sans-serif;
    color: var(--ink);
  }
  .contact__role {
    position: absolute;
    left: 15px; top: 43px;
    font: 400 11px/1 "Open Sans", sans-serif;
    color: var(--ink);
  }
  .contact__line {
    position: absolute;
    left: 15px;
    display: flex;
    align-items: center;
    gap: 8px;
    line-height: 1;
    font-family: "Open Sans", sans-serif;
    color: var(--ink);
  }
  .contact__line svg { fill: var(--ink-soft); }
  .contact__line--phone { top: 67px; font-size: 15px; }
  .contact__line--email { top: 97px; font-size: 11.5px; }
  .contact__line--web   { top: 118px; font-size: 11.5px; }

  .brand-front {
    position: absolute;
    right: 14px; bottom: 22px;
    display: flex;
    flex-direction: column;
    align-items: center;
    gap: 18px;
  }
  .brand-front__ring {
    width: 84px; height: 84px;
    border: 4px solid var(--brand-brown);
    border-radius: 50%;
  }
  .brand-front__name {
    font: 700 16px/1 "Cinzel", serif;
    color: #2f2f2f;
    letter-spacing: 0.2px;
    white-space: nowrap;
  }

  .brand-back {
    position: absolute;
    left: 0; right: 0; top: 55px;
    display: flex;
    flex-direction: column;
    align-items: center;
  }
  .brand-back__ring {
    width: 130px; height: 130px;
    border: 4px solid var(--silver);
    border-radius: 50%;
  }
  .brand-back__name {
    margin-top: 8px;
    font: 700 24px/1 "Cinzel", serif;
    color: var(--silver);
    white-space: nowrap;
  }
  .brand-back__tagline {
    margin-top: 9px;
    font: 400 13px/1 "Open Sans", sans-serif;
    color: var(--silver-dim);
  }
</style>
</head>
<body>
<main class="canvas">
  <section class="card card--front" aria-label="Business card front">
    <h1 class="contact__name">Tovan Presfield</h1>
    <p class="contact__role">Director</p>

    <p class="contact__line contact__line--phone">
      <svg width="14" height="12" viewBox="0 0 14 12" aria-hidden="true">
        <path d="M1 4 C1 1.5 13 1.5 13 4 L13 5 L10 5 L10 3.8 L4 3.8 L4 5 L1 5 Z"/>
        <path d="M3 6 L11 6 L12.5 11 L1.5 11 Z"/>
      </svg>
      0427 31 94 62
    </p>
    <p class="contact__line contact__line--email">
      <svg width="11" height="8" viewBox="0 0 11 8" aria-hidden="true">
        <rect x="0" y="0" width="11" height="8"/>
        <path d="M0.5 0.5 L5.5 4.5 L10.5 0.5" fill="none" stroke="#f1f1f0" stroke-width="1"/>
      </svg>
      tovan@tp-advisory.com.au
    </p>
    <p class="contact__line contact__line--web">
      <svg width="11" height="11" viewBox="0 0 11 11" aria-hidden="true">
        <g fill="none" stroke="#555" stroke-width="1">
          <circle cx="5.5" cy="5.5" r="4.8"/>
          <ellipse cx="5.5" cy="5.5" rx="2.2" ry="4.8"/>
          <line x1="0.7" y1="5.5" x2="10.3" y2="5.5"/>
        </g>
      </svg>
      www.tp-advisory.com.au
    </p>

    <div class="brand-front">
      <span class="brand-front__ring" aria-hidden="true"></span>
      <p class="brand-front__name">TP Advisory Services</p>
    </div>
  </section>

  <section class="card card--back" aria-label="Business card back">
    <div class="brand-back">
      <span class="brand-back__ring" aria-hidden="true"></span>
      <p class="brand-back__name">TP Advisory Services</p>
      <p class="brand-back__tagline">Clear Advice, Steady Delivery, Lasting Value</p>
    </div>
  </section>
</main>
</body>
</html>
```